Corvenly Postbox Website Concept (3 Pages)

We're looking to take this website: http://www.corvenlypostbox.example, and redesign it to be more e-commerce oriented. We'd also like to incorporate a seperate page for a blog. The key target is retail customers.
We're looking for a design that has e-commerce like: http://www.trindomart.example/mailboxes.htm?r=1, but still has the homey, stylish feel of: https://quillharbox.example/.
+Pages To Be Designed:
-Home Page
-Product Page
-Main Shopping Page
+Colors:
Attached in files is the color, please make the 'marine' the primary color.
+Home Page
-Incorporate the information from the Residential and Commercial pages on the original website
-Seal or Banner that says Veteran Owned Business
-Seal or Banner that show we are eco-friendly
-Social media link
-DO NOT worry about a gallery page from the original website
-Testimonial section
Target Market(s)
Retail customers
Industry/Entity Type
Sales
Number of Pages Required
3 page
Requirements
Must have
- +Pages To Be Designed:
- -Home Page
- -Product Page
- -Main Shopping Page
- +Home Page
- -Incorporate the information from the Residential and Commercial pages on the original website
- -Seal or Banner that says Veteran Owned Business
- -Seal or Banner that shows we are eco-friendly
- -Testimonial section
Nice to have
- -Social media link s

```html
<!DOCTYPE html>
<html lang="en">
<head>
<meta charset="utf-8">
<title>Corvenly Postbox</title>
<link href="https://fonts.googleapis.com/css2?family=Roboto:ital,wght@0,300;0,400;0,500;0,700;1,400&display=swap" rel="stylesheet">
<style>
:root{
  --marine:#4cb88a;
  --marine-dark:#3aa276;
  --ink:#2e2e2e;
  --muted:#6b6b6b;
  --soft:#f3f4f5;
  --line:#e2e2e2;
  --white:#ffffff;
}
*{box-sizing:border-box;margin:0;padding:0}
html,body{width:1200px;height:3141px;overflow:hidden}
body{font-family:'Roboto',sans-serif;color:var(--ink);background:var(--white);position:relative}
.abs{position:absolute}
a{color:inherit;text-decoration:none}

/* hero */
.hero{position:absolute;left:0;top:0;width:1200px;height:545px;
  background:linear-gradient(180deg,#5f7a4a 0%,#7d8f5c 30%,#6b5a45 60%,#8a8470 78%,#9c9a8c 100%)}
.brand-tab{position:absolute;left:63px;top:0;width:178px;height:157px;background:var(--marine);
  display:flex;flex-direction:column;align-items:center;justify-content:flex-end;padding-bottom:26px;gap:14px}
.brand-tab .mark{width:30px;height:30px;background:var(--white)}
.brand-name{font-weight:700;font-size:17px;color:var(--white)}
.main-nav{position:absolute;top:25px;left:415px;display:flex;gap:46px;font-size:14px;font-weight:500;color:var(--white)}
.pill{position:absolute;top:19px;height:27px;border-radius:14px;font-size:12px;display:flex;align-items:center;justify-content:center}
.pill-shop{left:959px;width:71px;background:var(--white);color:var(--ink)}
.pill-dealer{left:1041px;width:121px;background:var(--white);color:var(--ink)}

.learn-bar{position:absolute;left:0;top:545px;width:1200px;height:31px;background:#eeeeee;
  display:flex;align-items:center;padding:0 52px;font-size:12px;color:var(--muted);gap:20px}
.learn-bar .label{margin-right:-8px}
.learn-bar .social{margin-left:auto;display:flex;gap:26px;align-items:center}
.sq{width:15px;height:15px;border-radius:2px}

/* intro */
.intro{position:absolute;left:0;top:576px;width:1200px;height:167px;text-align:center}
.intro .lead{margin-top:14px;font-size:20px;line-height:28px;color:var(--ink)}
.intro .sub{margin-top:6px;font-size:12px;color:var(--muted)}
.btn-outline{display:inline-flex;align-items:center;gap:8px;margin-top:20px;height:36px;padding:0 26px;border:2px solid var(--marine);
  border-radius:18px;color:var(--marine);font-size:13px;font-weight:700}
.seal{position:absolute;top:28px;width:104px;height:104px;border-radius:50%;border:3px solid var(--marine);
  display:flex;align-items:center;justify-content:center;text-align:center;
  font-size:11px;font-weight:700;line-height:14px;color:var(--marine);padding:0 12px;text-transform:uppercase}
.seal::before{content:"";position:absolute;inset:5px;border-radius:50%;border:1px dashed var(--marine)}

.section-title{position:absolute;left:0;width:1200px;text-align:center;font-size:22px;font-weight:700}
.section-title span{color:var(--marine)}
.dotted{position:absolute;left:52px;width:1096px;border-top:2px dotted #cfd8d3}

/* services */
.services{position:absolute;left:0;top:743px;width:1200px;height:413px;background:var(--soft)}
.service{position:absolute;top:0;width:340px;text-align:center}
.service svg{position:absolute;top:132px;left:135px}
.service h3{position:absolute;top:235px;width:100%;font-size:18px;font-weight:700}
.service p{position:absolute;top:276px;left:0;width:340px;font-size:12px;line-height:17px;color:var(--muted)}
.connector{position:absolute;top:170px;height:1px;width:149px;background:#c8c8c8}

/* work */
.work-grid{position:absolute;left:0;top:1242px;width:1200px;height:318px;display:flex}
.work-tile{flex:1;height:100%}
.btn-solid{position:absolute;height:38px;background:var(--marine);color:var(--white);font-size:13px;font-weight:700;
  display:flex;align-items:center;justify-content:center;border-radius:3px}

/* news */
.news{position:absolute;left:0;top:1675px;width:1200px;height:534px;background:var(--soft)}
.card{position:absolute;top:117px;width:254px;height:354px;background:var(--white)}
.card .photo{height:189px}
.card h4{margin:20px 18px 0;font-size:18px;font-weight:700}
.card p{margin:10px 18px 0;font-size:12px;line-height:16px;color:var(--muted)}
.card .meta{position:absolute;left:18px;right:18px;bottom:18px;border-top:1px solid var(--line);padding-top:12px;
  display:flex;justify-content:space-between;font-size:11px;color:var(--muted)}

/* testimonials */
.quote{position:absolute;width:404px;font-size:12px;line-height:17px;font-style:italic;color:var(--muted)}
.quote.left{text-align:right}
.quote .who{margin-top:10px;font-style:normal;color:var(--ink);font-size:12px}
.avatar{position:absolute;width:76px;height:76px;border-radius:50%;background:radial-gradient(circle,#d8c3b0 0%,#c9ad96 55%,#eeeeee 56%);box-shadow:0 0 0 4px #f1f1f1}

/* contact */
.contact{position:absolute;left:0;top:2622px;width:1200px;height:352px;background:var(--soft)}
.contact h5{position:absolute;top:40px;font-size:18px;font-weight:700}
.field{position:absolute;height:32px;background:var(--white);border:1px solid var(--line);font-size:11px;color:#999;padding:9px 12px;border-radius:3px}
.map{position:absolute;left:333px;top:85px;width:534px;height:221px;background:linear-gradient(135deg,#dfe8d8 0%,#e8e6df 50%,#b9d8e6 100%)}
.info{position:absolute;left:896px;width:252px;font-size:12px;line-height:18px;color:var(--muted)}
.dot-btn{width:26px;height:26px;border-radius:50%;background:var(--marine)}

/* footer */
.footer-rule{position:absolute;left:0;top:2974px;width:1200px;height:3px;background:var(--marine)}
.footer-tab{position:absolute;left:932px;top:2998px;width:268px;height:40px;background:var(--marine);
  clip-path:polygon(0 0,100% 0,100% 100%,40px 100%);display:flex;align-items:center;justify-content:flex-end;padding-right:26px;gap:10px}
.footer-tab .mark{width:18px;height:18px;background:var(--white)}
.footer-tab span{color:var(--white);font-weight:700;font-size:14px}
.foot-nav{position:absolute;top:3024px;left:52px;display:flex;align-items:center;gap:26px;font-size:13px;font-weight:500}
.foot-small{position:absolute;top:3067px;font-size:11px;color:var(--muted);display:flex;gap:20px}
.bottom-band{position:absolute;left:0;top:3134px;width:1200px;height:7px;background:var(--marine)}
</style>
</head>
<body>

<header class="hero" role="img" aria-label="Photo of a stone mailbox pillar in a landscaped front yard with a house and a vintage car">
  <div class="brand-tab"><div class="mark"></div><div class="brand-name">Corvenly Postbox</div></div>
  <nav class="main-nav"><a>RESIDENTIAL</a><a>OUR PRODUCTS</a><a>COMMERCIAL</a></nav>
  <a class="pill pill-shop">&#128722;&nbsp;Shop</a>
  <a class="pill pill-dealer">Become a Dealer</a>
</header>

<div class="learn-bar">
  <span class="label">Learn More:</span><a>Our Company</a><a>Gallery</a><a>Blog</a><a>Help &amp; Contact</a>
  <div class="social">
    <div class="sq" style="background:#3b5998"></div>
    <div class="sq" style="background:#1da1f2"></div>
    <div class="sq" style="background:#dd4b39"></div>
    <svg width="14" height="14" viewBox="0 0 14 14"><circle cx="6" cy="6" r="4.5" fill="none" stroke="#777" stroke-width="1.6"/><line x1="9.3" y1="9.3" x2="13" y2="13" stroke="#777" stroke-width="1.8"/></svg>
  </div>
</div>

<section class="intro">
  <div class="seal" style="left:70px">Veteran Owned Business</div>
  <p class="lead">We are a veteran owned full service mailbox company. Our fabrication team can match<br>Any mailbox system. We are the #1 mailbox provider in the mid south.</p>
  <p class="sub">See some of the features below and learn why People trust Corvenly Postbox</p>
  <a class="btn-outline">&#128722; SHOP MAILBOX</a>
  <div class="seal" style="right:70px">Eco Friendly Materials</div>
</section>

<section class="services">
  <h2 class="section-title" style="top:22px">Our <span>Services</span></h2>
  <div class="dotted" style="top:62px"></div>
  <div class="connector" style="left:339px"></div>
  <div class="connector" style="left:714px"></div>

  <div class="service" style="left:54px">
    <svg width="70" height="70" viewBox="0 0 70 70" fill="none" stroke="#4cb88a" stroke-width="2.4"><rect x="14" y="14" width="28" height="52"/><rect x="42" y="32" width="18" height="34"/><line x1="20" y1="6" x2="36" y2="6"/><line x1="28" y1="6" x2="28" y2="14"/><path d="M20 24h4M32 24h4M20 34h4M32 34h4M20 44h4M32 44h4M48 42h6M48 52h6"/><rect x="24" y="54" width="8" height="12"/></svg>
    <h3>Commercial</h3>
    <p>Whether you are a property manager, Architect or commercial developer, our full line of NPS Approved postal specialties from Brannoway manufacturing company will add value and convenience to your buildings mail system.</p>
  </div>
  <div class="service" style="left:430px">
    <svg width="70" height="70" viewBox="0 0 70 70" fill="none" stroke="#4cb88a" stroke-width="2.4"><path d="M10 22h50l-4-10H14z"/><rect x="14" y="22" width="42" height="44"/><rect x="20" y="30" width="10" height="10"/><rect x="40" y="30" width="10" height="10"/><rect x="29" y="48" width="12" height="18"/></svg>
    <h3>Residential</h3>
    <p>Durable, Rust free, and field repairable are just a few of the reasons we feature Stellwick Mailboxes. Our mailboxes add "Curb Appeal" to your Home or Development, while matching street signs provide the finishing touches.</p>
  </div>
  <div class="service" style="left:805px">
    <svg width="70" height="70" viewBox="0 0 70 70" fill="none" stroke="#4cb88a" stroke-width="2.6"><rect x="16" y="4" width="40" height="62" rx="3"/><rect x="23" y="12" width="26" height="14"/><path d="M23 36h26M23 44h26M23 52h26"/></svg>
    <h3>Customize your own</h3>
    <p>Realizing not everyone's taste is the same we want to allow you to mix it up a little. Because we know everyone has one of our mailboxes, (or they should) you can have yours a little different.</p>
  </div>
</section>

<h2 class="section-title" style="top:1171px">Our <span>Work</span></h2>
<div class="dotted" style="top:1212px"></div>
<div class="work-grid">
  <div class="work-tile" role="img" aria-label="House roof with a flag against blue sky" style="background:linear-gradient(180deg,#6c8fc9 0%,#9fb4d8 45%,#3a3b3f 70%,#2c2c2e 100%)"></div>
  <div class="work-tile" role="img" aria-label="Delivery truck beside a tractor carrying mailbox units" style="background:linear-gradient(180deg,#5f90cf 0%,#c9cfd6 45%,#6f7a50 70%,#d2562d 100%)"></div>
  <div class="work-tile" role="img" aria-label="New mailbox post on a suburban street" style="background:linear-gradient(180deg,#7ea7d8 0%,#b9cbe2 40%,#7aa350 62%,#8f8f8c 100%)"></div>
  <div class="work-tile" role="img" aria-label="Black mailbox post beside a sidewalk and truck" style="background:linear-gradient(180deg,#a8b8c6 0%,#e1e3e0 40%,#6e9447 65%,#b9b7b0 100%)"></div>
  <div class="work-tile" role="img" aria-label="Black street sign post at a neighborhood corner" style="background:linear-gradient(180deg,#5c8ed0 0%,#9ab9de 40%,#4d7a36 70%,#3f6a2b 100%)"></div>
</div>
<a class="btn-solid" style="left:540px;top:1600px;width:120px">LOAD MORE</a>

<section class="news">
  <h2 class="section-title" style="top:24px">Latest <span>News &amp; Views</span></h2>

  <article class="card" style="left:52px">
    <div class="photo" role="img" aria-label="Person walking through a doorway carrying a bag" style="background:linear-gradient(135deg,#e7e2dc 0%,#7b5a3e 55%,#3e2a1b 100%)"></div>
    <h4>Standard Post</h4>
    <p>Enim congue blandit. Lorem ipsum dolor sit amet, consectetur adipiscing elit. Quisque...</p>
    <div class="meta"><span>&#9638; 22 June, 2015</span><span>&#9646; 0</span></div>
  </article>
  <article class="card" style="left:333px">
    <div class="photo" role="img" aria-label="Glass coffee maker on a table" style="background:linear-gradient(135deg,#d9d3c9 0%,#a99c88 60%,#6f6353 100%)"></div>
    <h4>Video Post</h4>
    <p>Ultrices posuere cubilia curae curabitur sit amet tortor ut massa commodo. Vestibulum...</p>
    <div class="meta"><span>&#9638; 22 June, 2015</span><span>&#9646; 0</span></div>
  </article>
  <article class="card" style="left:614px">
    <div class="photo" role="img" aria-label="Cafe table and chairs against a brick wall" style="background:linear-gradient(135deg,#8c4a32 0%,#a9694a 50%,#5a3526 100%)"></div>
    <h4>Post with Image</h4>
    <p>Enim congue blandit. Lorem ipsum dolor sit amet, consectetur adipiscing elit. Quisque...</p>
    <div class="meta"><span>&#9638; 22 June, 2015</span><span>&#9646; 0</span></div>
  </article>
  <article class="card" style="left:894px">
    <div class="photo" role="img" aria-label="Leather wallet on a patterned cloth" style="background:linear-gradient(135deg,#e2d6c4 0%,#b59878 55%,#7a5538 100%)"></div>
    <h4>Image Post</h4>
    <p>Ultrices posuere cubilia curae curabitur sit amet tortor ut massa commodo. Vestibulum...</p>
    <div class="meta"><span>&#9638; 22 June, 2015</span><span>&#9646; 3</span></div>
  </article>
</section>

<h2 class="section-title" style="top:2235px">What <span>People Say</span></h2>
<div class="dotted" style="top:2274px"></div>
<div class="abs" style="left:600px;top:2310px;height:250px;border-left:2px dotted #9fd6bd"></div>
<div class="abs" style="left:52px;top:2440px;width:1096px;border-top:2px dotted #9fd6bd"></div>

<div class="quote left" style="left:57px;top:2326px">Duis aute irure dolor in reprehenderit in voluptate velit esse cillum dolore eu fugiat nulla pariatur. Excepteur sint occaecat cupidatat non proident, sunt in culpa qui officia deserunt mollit.<div class="who">Reid Halloway, Operations Manager</div></div>
<div class="avatar" role="img" aria-label="Portrait of the reviewer" style="left:492px;top:2320px"></div>
<div class="avatar" role="img" aria-label="Portrait of the reviewer" style="left:632px;top:2320px"></div>
<div class="quote" style="left:740px;top:2326px">Provident, similique sunt in culpa qui officia deserunt mollitia animi, id est laborum et dolorum fuga. Et harum quidem rerum facilis est et expedita distinctio. Nam libero tempore, cum soluta nobis.<div class="who">Nora Pelletier, Creative Designer</div></div>

<div class="quote left" style="left:57px;top:2472px">Luis aute irure dolor in reprehenderit in pluptate velit esse cillum dolore eu fugiat nulla pariatur. Excepteur sint occaecat cupidatat non proident, sunt in culpa qui officia deserunt mollit.<div class="who">Ines Varkov, Manager</div></div>
<div class="avatar" role="img" aria-label="Portrait of the reviewer" style="left:492px;top:2468px"></div>
<div class="avatar" role="img" aria-label="Portrait of the reviewer" style="left:632px;top:2468px"></div>
<div class="quote" style="left:740px;top:2472px">At vero eos et accusamus et iusto odio dignissimos ducimus qui blanditiis praesentium voluptatum deleniti atque corrupti quos dolores et quas molestias excepturi sint occaecati asperiores.<div class="who">Owen Brisket, Developer</div></div>

<section class="contact">
  <h5 style="left:52px">Feel Free to Mail</h5>
  <div class="field" style="left:52px;top:100px;width:118px">Name *</div>
  <div class="field" style="left:186px;top:100px;width:118px">Email *</div>
  <div class="field" style="left:52px;top:152px;width:252px">Subject</div>
  <div class="field" style="left:52px;top:188px;width:252px;height:70px">Write Your Message Here...</div>
  <a class="btn-solid" style="left:52px;top:278px;width:138px;height:32px;border-radius:16px;font-size:12px">SEND MESSAGE</a>

  <h5 style="left:0;width:1200px;text-align:center">Headquarters</h5>
  <div class="map" role="img" aria-label="Street map showing the headquarters location by the harbor"></div>

  <h5 style="left:896px">Contact Info</h5>
  <div class="info" style="top:78px">Our staff is available to you from 9AM until 5PM on weekdays.</div>
  <div class="info" style="top:128px">Phone: +1 (800) 555 01 42</div>
  <div class="info" style="top:156px">Office: Harbor Lane Exhibit Hall</div>
  <div class="info" style="top:184px">Email: info@corvenlypostbox.example</div>
  <h5 style="left:896px;top:234px">Follow Us on</h5>
  <div class="abs" style="left:896px;top:278px;display:flex;gap:12px">
    <div class="dot-btn"></div><div class="dot-btn"></div><div class="dot-btn"></div><div class="dot-btn"></div><div class="dot-btn"></div>
  </div>
</section>

<div class="footer-rule"></div>
<div class="footer-tab"><div class="mark"></div><span>Corvenly Postbox</span></div>
<nav class="foot-nav">
  <svg width="14" height="14" viewBox="0 0 14 14"><circle cx="6" cy="6" r="4.5" fill="none" stroke="#555" stroke-width="1.6"/><line x1="9.3" y1="9.3" x2="13" y2="13" stroke="#555" stroke-width="1.8"/></svg>
  <a>Help &amp; Contact</a><a>Our Products</a><a>Gallery</a><a>Blog</a><a>Shop</a>
</nav>
<div class="foot-small" style="left:52px"><a>About</a><a>Blog</a><a>Careers</a><a>Public Policy</a><a>Sitemap</a><a>People</a><a>Partners</a></div>
<div class="foot-small" style="right:52px"><span>&copy; 2006 - 2018</span><a>Privacy</a><a>Legal</a><a>Feedback</a></div>
<div class="bottom-band"></div>

</body>
</html>
```